PTA Business Card

Seeking design for a business card, standard size. It is going to be for myself in regards to PTA - details:

Hollis Brantley Elementary School
PTA President
Peter Lund
563-555-0147
Lundy1984@mailbarn.example

Requirement:
Linkbook icon? "Hollis Brantley PTA Rusk"
Chirper thing? I am new to twitter so not sure what to put, here is the link:
https://twitter.example/HBRoversPTA

I was thinking on the front would be a notebook paper background? Not a requirement but was thinking it would look cool?

Total freedom here, let your creativity spread because I don't have any suggestions for design, sorry. Colors of school district are black and yellow.

Backside I am not sure exactly what to put on it.

```html
<!DOCTYPE html>
<html lang="en">
<head>
<meta charset="utf-8">
<title>Hollis Brantley PTA – Business Card</title>
<link href="https://fonts.googleapis.com/css2?family=Libre+Baskerville:wght@700&family=Kalam:wght@400;700&display=swap" rel="stylesheet">
<style>
  :root {
    --backdrop: #2b2b2b;
    --paper: #f8f1aa;
    --rule-blue: #b9c9d6;
    --margin-red: #e8806a;
    --ink-black: #111111;
    --ink-blue: #1f3f8f;
    --rule-grey: #8c8c8c;
    --lens-light: #eef3f6;
    --lens-mid: #c9d3da;
    --marble-dark: #141414;
    --marble-light: #5a5a5a;
    --label-white: #ffffff;
  }
  * { box-sizing: border-box; margin: 0; padding: 0; }
  html, body {
    width: 1159px; height: 1200px; overflow: hidden;
    background: var(--backdrop);
  }
  .sheet {
    width: 1159px; height: 1200px;
    display: flex; flex-direction: column; align-items: center;
    justify-content: center; gap: 20px;
  }
  .card {
    position: relative; width: 1000px; height: 571px; overflow: hidden;
  }

  /* ---------- Front: notebook paper ---------- */
  .card-front {
    background-color: var(--paper);
    background-image: repeating-linear-gradient(
      to bottom,
      transparent 0 38px,
      var(--rule-blue) 38px 40px);
    background-position: 0 12px;
  }
  .margin-line {
    position: absolute; left: 62px; top: 0; bottom: 0; width: 3px;
    background: var(--margin-red);
  }
  .school-title {
    position: absolute; left: 90px; right: 0; top: 40px;
    text-align: center;
    font-family: "Libre Baskerville", Georgia, serif; font-weight: 700;
    color: var(--ink-black); line-height: 1;
  }
  .school-title .school-name { display: block; font-size: 62px; letter-spacing: -1px; }
  .school-title .school-type { display: block; font-size: 37px; margin-top: 8px; }

  .grey-rule {
    position: absolute; left: 72px; right: 18px; height: 5px;
    background: var(--rule-grey);
  }
  .grey-rule.top { top: 228px; }
  .grey-rule.double {
    top: 392px; height: 10px; background: transparent;
    border-top: 4px solid var(--rule-grey); border-bottom: 3px solid var(--rule-grey);
  }

  .holder {
    position: absolute; left: 82px; top: 255px;
    font-family: "Kalam", cursive; color: var(--ink-blue);
  }
  .holder-name { font-size: 58px; line-height: 1.05; }
  .holder-role { font-size: 26px; line-height: 1.2; }

  .contact {
    position: absolute; left: 82px; top: 425px;
    font-family: "Kalam", cursive; color: var(--ink-blue);
    list-style: none;
  }
  .contact li { display: flex; align-items: center; gap: 14px; height: 52px; }
  .contact .phone { font-size: 34px; }
  .contact .email { font-size: 24px; }
  .contact svg { width: 36px; height: 36px; flex: none; }

  .lens-area {
    position: absolute; left: 588px; top: 412px; width: 124px; height: 124px;
    border-radius: 50%;
    background: radial-gradient(circle at 40% 35%, var(--lens-light), var(--lens-mid));
  }
  .network-names {
    position: absolute; left: 588px; top: 442px; width: 124px;
    list-style: none; text-align: center;
    font-family: "Kalam", cursive; font-size: 20px; line-height: 32px;
    color: var(--ink-blue);
  }
  .social {
    position: absolute; left: 726px; top: 424px; right: 22px;
    font-family: "Kalam", cursive; color: var(--ink-blue); list-style: none;
  }
  .social li { height: 52px; display: flex; align-items: center; white-space: nowrap; }
  .social .page { font-size: 22px; }
  .social .handle { font-size: 30px; }

  /* ---------- Back: composition cover ---------- */
  .card-back {
    background: radial-gradient(ellipse at 35% 40%, var(--marble-light), var(--marble-dark) 75%);
  }
  .cover-texture { position: absolute; inset: 0; }
  .cover-label {
    position: absolute; left: 620px; top: 330px; width: 320px; height: 185px;
    background: var(--label-white); border: 3px solid var(--ink-black);
    text-align: center; color: var(--ink-black); padding-top: 16px;
  }
  .cover-label .label-school {
    font-family: "Libre Baskerville", Georgia, serif; font-weight: 700; line-height: 1.1;
  }
  .cover-label .label-school span { display: block; }
  .cover-label .label-school .school-name { font-size: 24px; }
  .cover-label .label-school .school-type { font-size: 15px; }
  .label-line { height: 2px; background: var(--ink-black); margin: 8px 18px 0; }
  .cover-label .label-name {
    font-family: "Kalam", cursive; font-size: 30px; line-height: 1.2; margin-top: 2px;
  }
  .cover-label .label-role {
    font-family: "Libre Baskerville", Georgia, serif; font-weight: 700; font-size: 15px;
  }
</style>
</head>
<body>
<main class="sheet">

  <section class="card card-front" aria-label="Business card front">
    <div class="margin-line"></div>

    <h1 class="school-title">
      <span class="school-name">Hollis Brantley</span>
      <span class="school-type">Elementary School</span>
    </h1>

    <div class="grey-rule top"></div>

    <div class="holder">
      <p class="holder-name">Peter Lund</p>
      <p class="holder-role">PTA President</p>
    </div>

    <div class="grey-rule double"></div>

    <ul class="contact">
      <li class="phone">
        <svg viewBox="0 0 38 38" aria-hidden="true">
          <rect x="1" y="1" width="36" height="36" rx="7" fill="#2f8f87"/>
          <path d="M12 9c2 0 3 4 3 5s-2 2-2 3c1 3 4 6 7 7 1 0 2-2 3-2s5 1 5 3-2 4-4 4C16 29 9 22 9 13c0-2 1-4 3-4z" fill="#fff"/>
        </svg>
        563-555-0147
      </li>
      <li class="email">
        <svg viewBox="0 0 38 38" aria-hidden="true">
          <rect x="3" y="8" width="32" height="22" rx="3" fill="#fff" stroke="#4a86c5" stroke-width="2"/>
          <path d="M4 10l15 11 15-11" fill="none" stroke="#4a86c5" stroke-width="2"/>
        </svg>
        Lundy1984@mailbarn.example
      </li>
    </ul>

    <div class="lens-area" role="img" aria-label="Magnifying glass held over the social network links"></div>
    <ul class="network-names">
      <li>Linkbook</li>
      <li>Chirper</li>
    </ul>

    <ul class="social">
      <li class="page">Hollis Brantley PTA Rusk</li>
      <li class="handle">@HBRoversPTA</li>
    </ul>
  </section>

  <section class="card card-back" aria-label="Business card back">
    <div class="cover-texture" role="img" aria-label="Black and white marbled composition-notebook cover with silver binder rings along the left"></div>
    <div class="cover-label">
      <p class="label-school">
        <span class="school-name">Hollis Brantley</span>
        <span class="school-type">Elementary School</span>
      </p>
      <div class="label-line"></div>
      <p class="label-name">Peter Lund</p>
      <p class="label-role">PTA President</p>
    </div>
  </section>

</main>
</body>
</html>
```